Fundraising Study Day East of England. Lift the January blues!

A flyer to advertise a fundraising event of lectures for dental hygienists and therapists in support of the exemption campaign. Currently dental hygienists and therapists require a prescription to deliver certain treatment or recommend certain toothpastes. If we are successful in the campaign we will be able to treat patients without these restrictions.

Dental

```html
<!DOCTYPE html>
<html lang="en">
<head>
<meta charset="utf-8">
<title>Fundraising Study Day East of England – Flyer</title>
<link rel="stylesheet" href="https://fonts.googleapis.com/css2?family=Oswald:wght@500;600;700&family=Arimo:wght@400;700&display=swap">
<style>
  :root {
    --teal: #1b8b8c;
    --teal-dark: #146f70;
    --teal-light: #3fb0ae;
    --ink: #1e1e1e;
    --paper: #ffffff;
    --backdrop: #3b3b3d;
  }
  * { margin: 0; padding: 0; box-sizing: border-box; }
  html, body { width: 1200px; height: 776px; overflow: hidden; }
  body {
    background: var(--backdrop);
    font-family: "Arimo", Arial, sans-serif;
    color: var(--ink);
    position: relative;
  }
  .flyer {
    position: absolute;
    top: 38px;
    width: 520px;
    height: 700px;
    background: var(--paper);
    overflow: hidden;
  }
  .flyer--front { left: 50px; }
  .flyer--back { left: 630px; }
  .abs { position: absolute; }

  /* Front */
  .top-band { left: 0; top: 0; width: 100%; height: 14px; background: var(--teal); }
  .title { left: 24px; top: 24px; right: 24px; font-family: "Oswald", "Arial Narrow", sans-serif; color: var(--teal); text-transform: uppercase; line-height: 1; }
  .title__kicker { font-size: 24px; font-weight: 600; letter-spacing: 0.3px; }
  .title__main { font-size: 42px; font-weight: 700; margin-top: 6px; letter-spacing: 0.5px; }
  .hero { left: 0; top: 98px; width: 520px; height: 356px; }
  .description-tab { left: 0; top: 470px; width: 210px; height: 30px; }
  .tab-label { left: 24px; top: 474px; color: #fff; font-weight: 700; font-size: 19px; letter-spacing: 1px; }
  .description { left: 24px; right: 24px; top: 504px; font-size: 14.5px; line-height: 1.25; text-align: justify; }
  .footer-band { left: 0; width: 100%; background: var(--teal); color: #fff; text-align: center; font-size: 12.5px; line-height: 1.3; }
  .flyer--front .footer-band { top: 628px; height: 72px; padding-top: 14px; }

  /* Back */
  .event-photo { left: 0; top: 0; width: 520px; height: 150px; }
  .info-rule { left: 0; top: 182px; width: 100%; height: 3px; background: var(--teal); }
  .info-band { position: absolute; }
  .info-band--location { left: 0; top: 162px; width: 236px; height: 56px; }
  .info-band--datetime { left: 268px; top: 140px; width: 252px; height: 54px; }
  .info-tab { color: #fff; }
  .info-tab__head { font-weight: 700; font-size: 13.5px; letter-spacing: 0.6px; text-transform: uppercase; line-height: 1.2; }
  .info-tab__body { font-size: 10px; line-height: 1.25; margin-top: 3px; }
  .location { left: 26px; top: 169px; }
  .datetime { left: 300px; top: 146px; }
  .cost { left: 26px; top: 226px; font-size: 27px; font-weight: 700; color: var(--teal); }
  .agenda-heading { left: 44px; top: 266px; font-size: 27px; font-weight: 700; color: var(--teal); letter-spacing: 0.5px; }
  .agenda { font-size: 10.5px; line-height: 1.25; }
  .agenda--left { left: 60px; top: 350px; width: 200px; }
  .agenda--right { left: 286px; top: 216px; width: 210px; }
  .session { margin-bottom: 18px; }
  .session__time { font-weight: 700; }
  .session__speaker { font-weight: 700; }
  .break { font-weight: 700; font-size: 15px; margin-bottom: 6px; }
  .flyer--back .footer-band { top: 602px; height: 52px; padding-top: 10px; }
</style>
</head>
<body>

<article class="flyer flyer--front">
  <div class="abs top-band"></div>
  <header class="abs title">
    <div class="title__kicker">Fundraising Study Day East of England.</div>
    <div class="title__main">Lift the January Blues!</div>
  </header>

  <svg class="abs hero" viewBox="0 0 520 356">
    <rect x="0" y="0" width="520" height="5" fill="var(--teal)"/>
    <defs>
      <linearGradient id="clinicTone" x1="0" y1="0" x2="1" y2="1">
        <stop offset="0" stop-color="#e6ebec"/>
        <stop offset="0.55" stop-color="#b9c8ca"/>
        <stop offset="1" stop-color="#2f8d8c"/>
      </linearGradient>
    </defs>
    <rect x="0" y="12" width="520" height="290" fill="url(#clinicTone)" role="img" aria-label="Photo of dental hygienists in teal scrubs treating a patient in a clinic"/>
    <polygon points="200,12 520,12 520,190" fill="var(--teal)" opacity="0.9"/>
    <polygon points="330,12 520,12 520,90" fill="var(--teal-light)" opacity="0.7"/>
    <polygon points="0,230 140,302 0,302" fill="var(--teal)" opacity="0.85"/>
    <rect x="316" y="210" width="164" height="140" fill="#fff"/>
    <rect x="322" y="216" width="152" height="128" fill="#9fb8bb" role="img" aria-label="Photo of a hygienist at work with magnifying loupes"/>
  </svg>

  <svg class="abs description-tab" viewBox="0 0 210 30" aria-hidden="true">
    <polygon points="0,0 210,0 196,30 0,30" fill="var(--teal)"/>
  </svg>
  <div class="abs tab-label">DESCRIPTION</div>

  <p class="abs description">A fundraising event to support our exemptions project. The day will consist of a series of presentations ranging from the new ECPD to new technologies. The aim, being to enhance our learning and raise funds to support the exemptions campaign. The speaker line includes some of the UK and Irelands most respected dental professionals in our field.</p>

  <div class="abs footer-band">https://www.ticketvale.co.uk/e/fundrais-<br>ing-study-day-east-of-england-lift-the-january-blues-tickets-48201937</div>
</article>

<article class="flyer flyer--back">
  <svg class="abs event-photo" viewBox="0 0 520 150" role="img" aria-label="Photo of a speaker presenting to a seated audience in a bright seminar room">
    <defs>
      <linearGradient id="roomTone" x1="0" y1="0" x2="0" y2="1">
        <stop offset="0" stop-color="#eef2f4"/>
        <stop offset="0.5" stop-color="#c7cfd3"/>
        <stop offset="1" stop-color="#6f7478"/>
      </linearGradient>
    </defs>
    <rect width="520" height="150" fill="url(#roomTone)"/>
  </svg>

  <div class="abs info-rule"></div>
  <svg class="info-band info-band--location" viewBox="0 0 236 56" aria-hidden="true">
    <polygon points="0,0 236,0 218,56 0,56" fill="var(--teal)"/>
  </svg>
  <svg class="info-band info-band--datetime" viewBox="0 0 252 54" aria-hidden="true">
    <polygon points="18,0 252,0 252,54 0,54" fill="var(--teal)"/>
  </svg>

  <div class="abs info-tab location">
    <div class="info-tab__head">Location</div>
    <div class="info-tab__body">Harlow Court Hotel, Meridian Way<br>Hatfield, AL10 4QX</div>
  </div>
  <div class="abs info-tab datetime">
    <div class="info-tab__head">Date and Time</div>
    <div class="info-tab__body">Fri 19 January 2018<br>09:00 – 16:30 GMT</div>
  </div>

  <div class="abs cost">Cost - £101.48</div>
  <div class="abs agenda-heading">AGENDA</div>

  <div class="abs agenda agenda--left">
    <div class="session"><span class="session__time">9.30 - 10.15</span><br><span class="session__speaker">Clara Whitford:</span> Immediate past president of the DHTA will be updating us on all things ECPD</div>
    <div class="session"><span class="session__time">10.15 - 11.00</span><br><span class="session__speaker">Nadia Ellery:</span> Will provide an update on teeth whitening and explain how social media has impacted her business<br>Rosalind Marsh: Our internationally acclaimed speaker will update our knowledge of periodontal disease and nutrition and new technologies.</div>
  </div>

  <div class="abs agenda agenda--right">
    <div class="break">11.00 - 11.30 Break</div>
    <div class="session"><span class="session__time">11.30 - 13.00</span><br><span class="session__speaker">Bronagh Tully &amp; Lydia Croft:</span> Will be providing a combined presentation on 'Scaling your business and start to finish Sonexa techniques. The aim being to build our business with effective communications, systems and protocols. This sessions promises audience participation!</div>
    <div class="break">12 - 1400 lunch</div>
    <div class="session"><span class="session__time">14 - 15.00</span><br><span class="session__speaker">Sam Devani:</span> Save your back. All things posture.</div>
    <div class="break">15.00 - 15.30 Break</div>
    <div class="session"><span class="session__time">15.30 16.30 -</span><br><span class="session__speaker">Rosalind Marsh:</span> Our internationally acclaimed speaker will update our knowledge of periodontal disease and nutrition and new technologies.</div>
  </div>

  <div class="abs footer-band">https://www.ticketvale.co.uk/e/fundrais-<br>ing-study-day-east-of-england-lift-the-january-blues-tickets-48201937</div>
</article>

</body>
</html>
```